Broschüre für Energieberater
Zielgruppe
Unternehmen die zu den KMU´s gehören (kleine und mittlere Unternehmen) haben die Möglichkeit eine Energieberatung über die ZEKV fördern zu lassen. Diese Beratung wird durch unsere Ingenieure durchgeführt und ist für den Kunden völlig kostenneutral. Zum einen erhält er eine 80% Förderung von der ZEKV (Zentralstelle für Kostenausgleich und Versorgung) die restlichen 20% erhält der Kunde von uns als Gutschrift. Wir finanzieren uns somit nur über die Fördergelder des Bundes. Die Vorteile des Kunden sind: Verringerung von Steuern, Einsparung von mindestens 10% an Energie ohne zusätzliche Kosten und somit weniger C0² Ausstoss, was wiederum allen zugute kommt. Somit ein hohes Maß an Umweltbewusstsein! Alle Investitionen die für die Einsparung von Energie von Vorteil sind, werden vom Bund mit bis zu 200.000 Euro gefördert. Voraussetzung eine durchgeführte ZEKV Energieberatung. Somit eine win/win Situation für alle Beteiligten.
Aufgabenstellung
Das Design kann - muss - nicht an unsere Webseite : www.wattlinde-beratung.de angelehnt sein.

```html
<!DOCTYPE html>
<html lang="de">
<head>
<meta charset="utf-8">
<title>Broschüre Energieberatung – Innenseite</title>
<link rel="stylesheet" href="https://fonts.googleapis.com/css2?family=Oswald:wght@500;600&family=Arimo:wght@400;700&display=swap">
<style>
  :root {
    --bg: #3a3a3a;
    --paper: #f2f2f1;
    --paper-shade: #e4e4e3;
    --yellow: #e2cf2c;
    --yellow-deep: #d8c322;
    --ink: #1b1b1b;
    --grass-dark: #24461a;
    --grass-mid: #3f6f27;
    --grass-light: #6f9c41;
    --sky-top: #b9bccb;
    --sky-mid: #d6d8e2;
    --sky-bottom: #eceef2;
  }
  * { box-sizing: border-box; margin: 0; padding: 0; }
  html, body { width: 1200px; height: 801px; overflow: hidden; }
  body { background: var(--bg); font-family: "Arimo", Arial, sans-serif; color: var(--ink); }

  .brochure {
    position: absolute; left: 78px; top: 30px;
    width: 1044px; height: 740px;
    display: grid; grid-template-columns: repeat(3, 348px);
    background: var(--paper);
    box-shadow: 0 16px 40px rgba(0,0,0,.45);
  }
  .panel { position: relative; overflow: hidden; }
  .panel--left { background: linear-gradient(to right, var(--paper) 70%, #e8e8e7); }
  .panel--middle { background: linear-gradient(to right, #dcdcdb, var(--paper-shade) 25%, #ececeb); }
  .panel--right { background: var(--paper); }

  .photo-grass {
    position: absolute; top: 0; left: 0; width: 348px; height: 440px;
    background:
      radial-gradient(ellipse 60% 45% at 30% 30%, rgba(150,190,100,.55), transparent 70%),
      radial-gradient(ellipse 80% 60% at 70% 80%, rgba(20,45,15,.45), transparent 70%),
      linear-gradient(160deg, var(--grass-light), var(--grass-mid) 50%, var(--grass-dark));
  }
  .panel--middle .photo-grass {
    background:
      radial-gradient(ellipse 70% 50% at 40% 75%, rgba(150,190,100,.45), transparent 70%),
      linear-gradient(200deg, var(--grass-mid), var(--grass-light) 55%, var(--grass-dark));
  }

  .intro-box {
    position: absolute; top: 0; left: 0; width: 320px; height: 372px;
    background: var(--yellow); padding: 64px 26px 0 32px;
  }
  .intro-box h1 {
    font-family: "Oswald", "Arial Narrow", sans-serif; font-weight: 600;
    font-size: 42px; line-height: 1; margin-bottom: 22px;
  }
  .intro-box p { font-size: 17px; line-height: 1.4; }

  .benefits { position: absolute; left: 0; right: 0; padding: 0 26px 0 40px; }
  .panel--left .benefits { top: 478px; }
  .panel--middle .benefits { top: 468px; }
  .benefit { display: flex; gap: 10px; margin-bottom: 30px; }
  .benefit svg { flex: none; width: 20px; height: 20px; margin-top: 2px; }
  .benefit h3 {
    font-family: "Oswald", "Arial Narrow", sans-serif; font-weight: 500;
    font-size: 16px; line-height: 1.2; margin-bottom: 2px;
  }
  .benefit p { font-size: 14.5px; line-height: 1.3; }

  .photo-idea {
    position: absolute; top: 0; left: 0; width: 348px; height: 408px;
    background:
      radial-gradient(ellipse 40% 30% at 35% 25%, rgba(255,250,225,.75), transparent 70%),
      radial-gradient(ellipse 45% 35% at 55% 78%, rgba(170,120,95,.35), transparent 70%),
      linear-gradient(to bottom, var(--sky-top), var(--sky-mid) 55%, var(--sky-bottom));
  }
  .contact-box {
    position: absolute; top: 408px; left: 0; width: 348px; height: 332px;
    background: linear-gradient(160deg, var(--yellow), var(--yellow-deep));
    padding: 38px 26px 0 24px; overflow: hidden;
  }
  .contact-box h2 {
    font-family: "Oswald", "Arial Narrow", sans-serif; font-weight: 600;
    font-size: 24px; margin-bottom: 8px;
  }
  .contact-box p { font-size: 15px; line-height: 1.45; position: relative; }
  .contact-box .call { margin-top: 28px; }
  .contact-box .phone { font-weight: 700; }
  .contact-box .team { font-weight: 700; margin-top: 26px; }
  .brand-mark {
    position: absolute; right: -14px; bottom: 56px;
    font-family: "Oswald", "Arial Narrow", sans-serif; font-weight: 600;
    font-size: 92px; line-height: 1; color: rgba(150,135,20,.28);
    letter-spacing: -1px; white-space: nowrap;
  }
</style>
</head>
<body>
  <main class="brochure">
    <section class="panel panel--left">
      <div class="photo-grass" role="img" aria-label="Foto: Steckdose mit eingestecktem weißen Kabel auf grünem Rasen"></div>
      <div class="benefits">
        <div class="benefit">
          <svg viewBox="0 0 18 18" aria-hidden="true"><circle cx="9" cy="9" r="9" fill="var(--yellow)"/><path d="M5 9.3l2.6 2.6L13 6.4" fill="none" stroke="#fff" stroke-width="2"/></svg>
          <div><h3>Keine versteckten Kosten!</h3><p>Lorem ipsum dolor sit aLorem ipsum dolor sit amet, consectetur adipiscing elit.</p></div>
        </div>
        <div class="benefit">
          <svg viewBox="0 0 18 18" aria-hidden="true"><circle cx="9" cy="9" r="9" fill="var(--yellow)"/><path d="M5 9.3l2.6 2.6L13 6.4" fill="none" stroke="#fff" stroke-width="2"/></svg>
          <div><h3>Staatliche Fördermittel sichern</h3><p>Lorem ipsum dolor sit aLorem ipsum dolor sit amet, consectetur adipiscing elit.</p></div>
        </div>
      </div>
    </section>

    <section class="panel panel--middle">
      <div class="photo-grass" role="img" aria-label="Foto: Fortsetzung des weißen Kabels auf grünem Rasen"></div>
      <div class="intro-box">
        <h1>Ihr Vorteil</h1>
        <p>Erhalten Sie jetzt Ihre staatlich geförderte Energieberatung, lassen Sie sich von Anfang an von Experten begleiten und sparen Sie ab sofort Energie und damit bares Geld!</p>
      </div>
      <div class="benefits">
        <div class="benefit">
          <svg viewBox="0 0 18 18" aria-hidden="true"><circle cx="9" cy="9" r="9" fill="var(--yellow)"/><path d="M5 9.3l2.6 2.6L13 6.4" fill="none" stroke="#fff" stroke-width="2"/></svg>
          <div><h3>Bis zu 25% Energie &amp; Kosten einsparen</h3><p>Lorem ipsum dolor sit aLorem ipsum dolor sit amet, consectetur adipiscing elit.</p></div>
        </div>
        <div class="benefit">
          <svg viewBox="0 0 18 18" aria-hidden="true"><circle cx="9" cy="9" r="9" fill="var(--yellow)"/><path d="M5 9.3l2.6 2.6L13 6.4" fill="none" stroke="#fff" stroke-width="2"/></svg>
          <div><h3>Experten gesicherte Durchführung</h3><p>Lorem ipsum dolor sit aLorem ipsum dolor sit amet, consectetur adipiscing elit.</p></div>
        </div>
      </div>
    </section>

    <section class="panel panel--right">
      <div class="photo-idea" role="img" aria-label="Foto: leuchtende Glühbirne schwebt über einer geöffneten Hand vor hellem Himmel"></div>
      <div class="contact-box">
        <span class="brand-mark" aria-hidden="true">Wattlinde</span>
        <h2>Wir beraten Sie gerne!</h2>
        <p>Vereinbaren Sie gleich noch heute<br>einen Termin.</p>
        <p class="call">Rufen Sie uns an</p>
        <p class="phone">06221-4471029</p>
        <p class="team">Ihr Energieeffizienz Team</p>
      </div>
    </section>
  </main>
</body>
</html>
```